Baby prediction and advice cards, thank you notes, Baby shower invitations and diaper raffle tickets

Please see attached brief with description of the project.

*** Only apply if you are DETAIL ORIENTED and willing to read 100% the brief and the correction instructions (if required)***

*** Only apply if you are able to communicate in English 100%***

We need QUALITY over quantity

Contact us if you have questions.

Thank you

Target Market(s)

Expecting mothers and their families (Mothers, sisters)

Font styles to use
Sans Serif

Colors

Designer to choose colors to be used in the design.

Requirements
Must have
• Read the brief
Should not have
• Read the brief

```html
<!DOCTYPE html>
<html lang="en">
<head>
<meta charset="utf-8">
<title>Baby Shower Stationery Set</title>
<link href="https://fonts.googleapis.com/css2?family=Amatic+SC:wght@400;700&display=swap" rel="stylesheet">
<style>
  :root{
    --bg:#ececea;
    --card:#c8b899;
    --card-edge:#d6cab2;
    --ink:#ffffff;
    --mint:#a9d8cf;
    --cream:#e8dcc6;
    --shadow:rgba(0,0,0,.18);
  }
  *{box-sizing:border-box;margin:0;padding:0}
  html,body{width:1200px;height:1200px;overflow:hidden}
  body{background:var(--bg);font-family:"Amatic SC",sans-serif;color:var(--ink);position:relative}
  .card{position:absolute;background:var(--card);border:4px solid var(--card-edge);box-shadow:0 4px 12px var(--shadow)}
  .card::before{content:"";position:absolute;inset:8px;border:2px dashed var(--ink);pointer-events:none}
  .cloud{position:absolute;width:34px;height:22px;border-radius:14px 16px 10px 10px;background:var(--mint);opacity:.85}
  .cloud.cream{background:var(--cream)}
  .cloud.small{width:24px;height:15px}
  .bullet{display:inline-block;width:11px;height:11px;border-radius:50%;box-shadow:inset 3px -1px 0 0 var(--ink);margin-right:6px;flex:none}
  .field{display:flex;align-items:flex-end;font-size:19px;font-weight:700;white-space:nowrap;margin-bottom:9px}
  .field .line{flex:1;border-bottom:1.5px solid var(--ink);margin-left:6px;height:1px;margin-bottom:5px}
  .box{display:inline-block;width:20px;height:18px;border:1.5px solid var(--ink);vertical-align:middle;margin-left:6px}
  .rule{height:2px;background:var(--mint);margin:0 auto}
  .rule.white{background:var(--ink)}

  /* Prediction card */
  .prediction{left:60px;top:130px;width:540px;height:390px}
  .prediction .title{position:absolute;top:28px;left:0;right:0;text-align:center}
  .prediction .title h1{font-size:46px;font-weight:700;line-height:1;letter-spacing:2px}
  .prediction .title p{font-size:22px;font-weight:700;margin-top:2px}
  .prediction .col-left{position:absolute;left:40px;top:150px;width:220px}
  .prediction .col-right{position:absolute;left:280px;top:118px;width:225px}
  .choice-row{display:flex;font-size:19px;font-weight:700;margin-bottom:9px}
  .choice-row .opts{display:flex;flex-direction:column;gap:4px;margin-left:8px}
  .advice-lines{position:absolute;left:40px;top:325px;width:220px}

  /* Raffle ticket */
  .raffle{left:415px;top:545px;width:265px;height:140px;text-align:center}
  .raffle h2{font-size:22px;font-weight:700;margin-top:20px}
  .raffle .rule{width:150px;margin-top:2px}
  .raffle p{font-size:17px;font-weight:700;line-height:1.1;margin:8px 30px 4px 50px}
  .raffle .field{margin:6px 28px 0;font-size:16px}

  /* Invitation */
  .invite{left:60px;top:600px;width:340px;height:460px}
  .invite .head{text-align:center;margin-top:80px;line-height:.95}
  .invite .head .small{font-size:30px;font-weight:700;display:block}
  .invite .head .big{font-size:50px;font-weight:700;display:block;letter-spacing:3px}
  .invite .join{font-size:19px;font-weight:700;margin:8px 36px 10px}
  .invite .fields{margin:0 50px 0 36px}
  .invite .gap{height:18px}

  /* Folded thank-you card */
  .folded{left:700px;top:130px;width:480px;height:650px}
  .folded .fold{position:absolute;left:0;right:0;top:318px;border-top:2px solid var(--card-edge);box-shadow:0 -1px 0 rgba(0,0,0,.12)}
  .folded .front{position:absolute;left:0;right:0;top:320px;bottom:0;display:flex;align-items:center;justify-content:center}
  .folded .front h2{font-size:46px;font-weight:400;letter-spacing:3px}
  .folded .front .rule{width:230px;position:absolute;top:190px;left:125px}

  /* Message insert */
  .message{left:510px;top:810px;width:410px;height:260px;text-align:center}
  .message .rule{width:110px;margin-top:78px}
  .message .rule.white{width:160px;margin-top:6px}
  .message p{font-size:21px;font-weight:700;letter-spacing:1px;line-height:1.2;margin:14px 50px 0}
</style>
</head>
<body>

<section class="card prediction">
  <div class="cloud" style="left:30px;top:85px" role="img" aria-label="cloud doodle"></div>
  <div class="cloud cream small" style="left:70px;top:72px" role="img" aria-label="cloud doodle"></div>
  <div class="cloud cream" style="left:440px;top:42px" role="img" aria-label="cloud doodle"></div>
  <div class="cloud small" style="left:482px;top:30px" role="img" aria-label="cloud doodle"></div>
  <div class="cloud" style="left:222px;top:195px" role="img" aria-label="cloud doodle"></div>
  <div class="cloud cream" style="left:90px;top:272px" role="img" aria-label="cloud doodle"></div>
  <div class="title">
    <h1>Baby</h1>
    <div class="rule" style="width:120px"></div>
    <p>prediction and advice</p>
  </div>
  <div class="col-left">
    <div class="field"><span class="bullet"></span>Baby's name:<span class="line"></span></div>
    <div class="choice-row"><span class="bullet"></span>Gender:
      <span class="opts"><span>Boy<span class="box"></span></span><span>Girl<span class="box"></span></span></span>
      <span class="opts" style="margin-left:14px"><span>Weight:</span><span>Length:</span></span>
    </div>
    <div class="choice-row" style="margin-top:18px"><span class="bullet"></span>Resemblance:
      <span class="opts"><span>All dad<span class="box"></span></span><span>All mom<span class="box"></span></span><span>Both<span class="box" style="margin-left:12px"></span></span></span>
    </div>
  </div>
  <div class="advice-lines">
    <div class="field"><span class="bullet"></span>My best advice:<span class="line"></span></div>
    <div class="field"><span class="line" style="margin-left:0"></span></div>
  </div>
  <div class="col-right">
    <div class="field"><span class="bullet"></span>Date of birth:<span class="line"></span></div>
    <div class="field"><span class="bullet"></span>Time of birth:<span class="line"></span></div>
    <div class="field"><span class="bullet"></span>Hair color:<span class="line"></span></div>
    <div class="field"><span class="bullet"></span>Eye color:<span class="line"></span></div>
    <div class="field" style="margin-top:26px"><span class="bullet"></span>I hope you get dad's:<span class="line"></span></div>
    <div class="field"><span class="bullet"></span>I hope you get mom's:<span class="line"></span></div>
    <div class="field" style="margin-top:20px"><span class="bullet"></span>Best wishes and love from:<span class="line"></span></div>
    <div class="field"><span class="line" style="margin-left:0"></span></div>
  </div>
</section>

<section class="card raffle">
  <div class="cloud small" style="left:24px;top:62px" role="img" aria-label="cloud doodle"></div>
  <h2>Diaper Raffle Ticket</h2>
  <div class="rule"></div>
  <p>Bring a pack of diapers (any size) for your chance to win a prize!</p>
  <div class="field">Name:<span class="line"></span></div>
</section>

<section class="card invite">
  <div class="cloud" style="left:22px;top:22px" role="img" aria-label="cloud doodle"></div>
  <div class="cloud cream small" style="left:62px;top:30px" role="img" aria-label="cloud doodle"></div>
  <div class="cloud cream small" style="left:22px;top:58px" role="img" aria-label="cloud doodle"></div>
  <div class="cloud cream small" style="left:245px;top:395px" role="img" aria-label="cloud doodle"></div>
  <div class="cloud" style="left:262px;top:412px" role="img" aria-label="cloud doodle"></div>
  <div class="head">
    <span class="small">Celebrating</span>
    <span class="big">A Baby</span>
    <span class="small">on the way</span>
  </div>
  <div class="rule" style="width:140px;margin-top:4px"></div>
  <p class="join">"Join us for a shower honoring:</p>
  <div class="fields">
    <div class="field"><span class="bullet"></span>Time:<span class="line"></span></div>
    <div class="field"><span class="bullet"></span>Place:<span class="line"></span></div>
    <div class="field"><span class="bullet"></span>Details:<span class="line"></span></div>
    <div class="field"><span class="line" style="margin-left:17px"></span></div>
    <div class="gap"></div>
    <div class="field"><span class="bullet"></span>RSVP to:<span class="line"></span></div>
    <div class="field"><span class="bullet"></span>Hosted by:<span class="line"></span></div>
  </div>
</section>

<section class="card folded">
  <div class="cloud small" style="left:222px;top:50px" role="img" aria-label="cloud doodle"></div>
  <div class="fold"></div>
  <div class="front">
    <div class="cloud" style="left:40px;top:20px" role="img" aria-label="cloud doodle"></div>
    <div class="cloud cream small" style="left:80px;top:38px" role="img" aria-label="cloud doodle"></div>
    <div class="cloud cream small" style="left:30px;top:58px" role="img" aria-label="cloud doodle"></div>
    <div class="cloud cream small" style="left:380px;top:265px" role="img" aria-label="cloud doodle"></div>
    <div class="cloud" style="left:410px;top:275px;background:var(--ink)" role="img" aria-label="cloud doodle"></div>
    <h2>"Thank You"</h2>
    <div class="rule"></div>
  </div>
</section>

<section class="card message">
  <div class="cloud" style="left:22px;top:18px" role="img" aria-label="cloud doodle"></div>
  <div class="cloud cream small" style="left:62px;top:26px" role="img" aria-label="cloud doodle"></div>
  <div class="cloud cream small" style="left:22px;top:52px" role="img" aria-label="cloud doodle"></div>
  <div class="cloud small" style="left:350px;top:210px" role="img" aria-label="cloud doodle"></div>
  <div class="rule"></div>
  <div class="rule white"></div>
  <p>"For being with me and sharing in the celebration of this wonderful occasion."</p>
</section>

</body>
</html>
```